RESIDENTIAL CONSTRUCTION

We are a company that specializes in building custom residential homes, the design should also emphasize that quality and service is our priority.

Industry/Entity Type

Construction Company

Contact Information for Business Card

Contact Person: Tobias Kerrigan
Company Address: 243 West 9th St San Jose , Ca 95387
Phone Number : 408-736-2049
Email Address: Stonegatecrafts517@mailbrook.net

Font styles to use
Sans Serif

Colors
ec1f27

Requirements
Must have
• CSLB # 2736159
Nice to have
• needs to have same color as logo i uploaded, we will be printing these on a clear plastic card.

```html
<!DOCTYPE html>
<html lang="en">
<head>
<meta charset="utf-8">
<title>Keystone General Builders – Business Card</title>
<link rel="stylesheet" href="https://fonts.googleapis.com/css2?family=Montserrat:wght@700;800;900&family=Roboto:wght@400&display=swap">
<style>
  :root {
    --brand-red: #c1323a;
    --ink: #1f1f1f;
    --muted-ink: #4a4a4a;
    --icon-ink: #3b1518;
    --card: #ffffff;
    --backdrop: #e4e4e4;
  }
  * { margin: 0; padding: 0; box-sizing: border-box; }
  html, body {
    width: 1200px;
    height: 1200px;
    overflow: hidden;
    background: var(--backdrop);
  }
  .canvas {
    position: relative;
    width: 1200px;
    height: 1200px;
  }
  .business-card {
    position: absolute;
    left: 100px;
    top: 320px;
    width: 1000px;
    height: 560px;
    background: var(--card);
    border-radius: 40px;
    overflow: hidden;
    box-shadow: 0 18px 40px rgba(0,0,0,0.18);
  }

  /* Company name block */
  .company {
    position: absolute;
    left: 70px;
    top: 140px;
    display: flex;
    align-items: center;
    gap: 16px;
  }
  .company-mark {
    width: 56px;
    height: 56px;
    background: var(--brand-red);
  }
  .company-name {
    font-family: "Montserrat", sans-serif;
    font-weight: 800;
    color: var(--brand-red);
    text-transform: uppercase;
    line-height: 1;
  }
  .company-name .line-main { display: block; font-size: 44px; letter-spacing: 1px; }
  .company-name .line-sub { display: block; font-size: 16px; letter-spacing: 3.2px; margin-top: 6px; }

  /* Contact person */
  .person {
    position: absolute;
    left: 70px;
    top: 360px;
    text-transform: uppercase;
    font-family: "Montserrat", sans-serif;
    line-height: 1;
  }
  .person-first {
    display: block;
    font-weight: 900;
    font-size: 72px;
    color: var(--ink);
    letter-spacing: 2px;
  }
  .person-last {
    display: block;
    font-weight: 800;
    font-size: 30px;
    color: var(--brand-red);
    letter-spacing: 2px;
    margin-top: 6px;
    text-align: right;
  }
  .license {
    position: absolute;
    left: 70px;
    top: 490px;
    font-family: "Montserrat", sans-serif;
    font-weight: 700;
    font-size: 18px;
    letter-spacing: 1.5px;
    color: var(--muted-ink);
  }

  /* Contact bands */
  .accent-strip {
    position: absolute;
    left: 620px;
    top: 112px;
    right: 0;
    height: 22px;
    background: var(--brand-red);
  }
  .contact-list {
    position: absolute;
    left: 540px;
    top: 146px;
    right: 0;
    list-style: none;
    display: flex;
    flex-direction: column;
    gap: 10px;
  }
  .contact-row {
    display: flex;
    gap: 10px;
    height: 64px;
  }
  .contact-icon {
    flex: 0 0 64px;
    background: var(--brand-red);
    display: flex;
    align-items: center;
    justify-content: center;
  }
  .contact-icon svg { width: 26px; height: 26px; fill: var(--icon-ink); }
  .contact-text {
    flex: 1;
    background: var(--brand-red);
    color: #ffffff;
    font-family: "Roboto", Arial, sans-serif;
    font-size: 21px;
    display: flex;
    align-items: center;
    padding-left: 26px;
    white-space: nowrap;
  }
</style>
</head>
<body>
<main class="canvas">
  <section class="business-card">
    <div class="company">
      <div class="company-mark"></div>
      <div class="company-name">
        <span class="line-main">Keystone</span>
        <span class="line-sub">General Builders</span>
      </div>
    </div>

    <div class="person">
      <span class="person-first">Tobias</span>
      <span class="person-last">Kerrigan</span>
    </div>
    <p class="license">CSLB # 2736159</p>

    <div class="accent-strip"></div>
    <ul class="contact-list">
      <li class="contact-row">
        <span class="contact-icon">
          <svg viewBox="0 0 24 24" aria-hidden="true"><path d="M12 2a7 7 0 0 0-7 7c0 5 7 13 7 13s7-8 7-13a7 7 0 0 0-7-7zm0 9.5A2.5 2.5 0 1 1 12 6.5a2.5 2.5 0 0 1 0 5z"/></svg>
        </span>
        <span class="contact-text">243 West 9th St San Jose, Ca 95387</span>
      </li>
      <li class="contact-row">
        <span class="contact-icon">
          <svg viewBox="0 0 24 24" aria-hidden="true"><path d="M6.6 10.8a15 15 0 0 0 6.6 6.6l2.2-2.2a1 1 0 0 1 1-.25 11.4 11.4 0 0 0 3.6.57 1 1 0 0 1 1 1V20a1 1 0 0 1-1 1A17 17 0 0 1 3 4a1 1 0 0 1 1-1h3.5a1 1 0 0 1 1 1c0 1.25.2 2.45.57 3.57a1 1 0 0 1-.25 1z"/></svg>
        </span>
        <span class="contact-text">408-736-2049</span>
      </li>
      <li class="contact-row">
        <span class="contact-icon">
          <svg viewBox="0 0 24 24" aria-hidden="true"><path d="M3 5h18a1 1 0 0 1 1 1v12a1 1 0 0 1-1 1H3a1 1 0 0 1-1-1V6a1 1 0 0 1 1-1zm9 7.5L20.5 7h-17z"/></svg>
        </span>
        <span class="contact-text">Stonegatecrafts517@mailbrook.net</span>
      </li>
    </ul>
  </section>
</main>
</body>
</html>
```